Visitenkarten für Urologisches Zentrum Lindenhof
Zielgruppe
Urologisches Zentrum Lindenhof / Vasektomie-Zentrum Lindenhof
Aufgabenstellung
Bitte an der alten Vorlage orientieren. Die 1. Seite (Aussenseite der Klappkarte) ist in Ordnung.
2. Seite (Innenseite der Klappkarte): Hier ggf. eine besser lesbare Schrift.
Adresse: Dr. med. FELIX BRANDT &
Dr. med. MARTIN OSWALD
Birkenweg 17
68999 Musterstadt
Fon: unverändert, jedoch bitte etwas übersichtlicher
Fax: unverändert, jedoch bitte etwas übersichtlicher
E-Mail: unverändert, jedoch bitte etwas übersichtlicher
Web: unverändert, jedoch bitte etwas übersichtlicher
Öffnungszeiten: Mo,Di: 08:00 - 12:00 Uhr
14:00 - 16:00 Uhr
Mi: 08:00 - 12:00 Uhr
Do,Fr: 08.00 - 12:00 Uhr
Es sollte noch folgender Text eingefügt werden: Wußten Sie schon? Sie können bei uns Termine über www.terminofix.de
vereinbaren.
Bitte machen Sie uns einige dynamischere Gestaltungsvorschläge. Die Karte sollte in weiß gehalten werden. Keine Glanzbeschichtung und etwas kräftigeres, hochwertiges Papier.
Ich freue mich auf Ihre Vorschläge.

```html
<!DOCTYPE html>
<html lang="de">
<head>
<meta charset="utf-8">
<title>Visitenkarten – Urologisches Zentrum Lindenhof</title>
<link href="https://fonts.googleapis.com/css2?family=Arimo:wght@400;700&family=Montserrat:wght@600&display=swap" rel="stylesheet">
<style>
  :root{
    --bg:#e4e2e0;
    --card:#f3f3f3;
    --green:#7aab4f;
    --ink:#3a3a3a;
    --muted:#6b6b6b;
    --rule:#8a8a8a;
    --edge:#9a9a9a;
  }
  *{box-sizing:border-box;margin:0;padding:0}
  html,body{width:1200px;height:1200px;overflow:hidden;background:var(--bg)}
  body{position:relative;font-family:"Arimo",Arial,sans-serif;color:var(--ink)}
  .card{position:absolute;width:520px;height:336px;background:var(--card);
        box-shadow:0 6px 18px rgba(0,0,0,.12);overflow:hidden}
  .card--contact{left:60px;top:180px}
  .card--hours{left:620px;top:180px}
  .card--combined{left:340px;top:640px}

  .brand{position:absolute;display:flex;align-items:center;gap:10px}
  .brand__dot{width:26px;height:26px;border-radius:50%;background:var(--green);flex:none}
  .brand__name{font-family:"Montserrat",Arial,sans-serif;font-weight:600;font-size:15px;
               letter-spacing:.06em;text-transform:uppercase;color:var(--ink);white-space:nowrap}
  .brand__rule{position:absolute;height:1.5px;background:var(--rule)}

  .org{position:absolute;font-weight:700;font-size:11px;line-height:1.35}
  .org__rule{position:absolute;height:1.5px;background:var(--rule)}
  .fields{position:absolute;display:grid;grid-template-columns:auto 10px auto;
          font-size:11px;line-height:1.45;column-gap:2px}
  .fields dt{color:var(--green);font-weight:700}
  .fields .sep{color:var(--muted)}
  .fields dd{color:var(--ink)}

  .stripe{position:absolute;left:0;bottom:18px;height:6px;width:440px;background:var(--green)}
  .stripe-end{position:absolute;left:450px;bottom:18px;height:6px;width:70px;background:var(--edge)}

  .hours-title{position:absolute;font-weight:700;font-size:14px}
  .hours-rule{position:absolute;height:1.5px;background:var(--rule)}
  .hours{position:absolute;display:grid;grid-template-columns:34px 12px auto;
         font-size:13px;line-height:1.55}
  .hours dt{color:var(--green);font-weight:700}
  .hours .sep{color:var(--muted)}

  .notice{position:absolute;left:0;right:0;bottom:0;height:86px;background:var(--green);
          color:#fff;font-size:14px;line-height:1.5;text-align:center;
          display:flex;flex-direction:column;justify-content:center}
  .notice--plain{background:none;color:var(--ink);height:auto;bottom:30px;font-size:11px}
</style>
</head>
<body>

  <!-- Vorderseite: Kontakt -->
  <section class="card card--contact">
    <div class="brand" style="right:34px;top:42px">
      <span class="brand__dot"></span>
      <span class="brand__name">Urologisches Zentrum Lindenhof</span>
    </div>
    <div class="brand__rule" style="right:34px;top:78px;width:330px"></div>

    <div class="org" style="left:34px;top:122px">
      Urologisches Zentrum Lindenhof (UZL)<br>Vasektomie-Zentrum Lindenhof
    </div>
    <div class="org__rule" style="left:34px;top:156px;width:215px"></div>

    <dl class="fields" style="left:34px;top:166px">
      <dt>Adresse</dt><span class="sep">:</span>
      <dd>Dr. med. FELIX BRANDT &amp;<br>Dr. med. MARTIN OSWALD<br>Birkenweg 17<br>68999 Musterstadt</dd>
    </dl>

    <dl class="fields" style="left:290px;top:180px">
      <dt>Fon</dt><span class="sep">:</span><dd>0621 555 0128 &nbsp;|&nbsp; 0621 555 0650</dd>
      <dt>Fax</dt><span class="sep">:</span><dd>0621 555 0129</dd>
      <dt>E-Mail</dt><span class="sep">:</span><dd>praxis@lindenhof-uro.de</dd>
      <dt>Web</dt><span class="sep">:</span><dd>www.lindenhof-uro.de</dd>
    </dl>

    <div class="stripe"></div>
    <div class="stripe-end"></div>
  </section>

  <!-- Rückseite: Öffnungszeiten -->
  <section class="card card--hours">
    <h2 class="hours-title" style="left:34px;top:34px">Öffnungszeiten</h2>
    <div class="hours-rule" style="left:34px;top:56px;width:452px"></div>
    <dl class="hours" style="left:60px;top:72px">
      <dt>Mo</dt><span class="sep">:</span><dd>08:00 - 12:00 Uhr</dd>
      <dt>Di</dt><span class="sep">:</span><dd>14:00 - 16:00 Uhr</dd>
      <dt>Mi</dt><span class="sep">:</span><dd>08:00 - 12:00 Uhr</dd>
      <dt>Do</dt><span class="sep">:</span><dd>08.00 - 12:00 Uhr</dd>
      <dt>Fr</dt><span class="sep">:</span><dd>14:00 - 16:00 Uhr</dd>
    </dl>
    <p class="notice">
      <span>Wußten Sie schon? Sie können bei uns Termine über</span>
      <span>www.terminofix.de vereinbaren</span>
    </p>
  </section>

  <!-- Variante: Logo mit Öffnungszeiten -->
  <section class="card card--combined">
    <div class="brand" style="left:50%;transform:translateX(-50%);top:50px">
      <span class="brand__dot"></span>
      <span class="brand__name">Urologisches Zentrum Lindenhof</span>
    </div>
    <div class="brand__rule" style="left:95px;top:86px;width:330px"></div>

    <h2 class="hours-title" style="left:34px;top:146px;font-size:12px">Öffnungszeiten</h2>
    <div class="hours-rule" style="left:34px;top:165px;width:170px"></div>
    <dl class="hours" style="left:50px;top:176px;font-size:11px">
      <dt>Mo</dt><span class="sep">:</span><dd>08:00 - 12:00 Uhr</dd>
      <dt>Di</dt><span class="sep">:</span><dd>14:00 - 16:00 Uhr</dd>
    </dl>
    <dl class="hours" style="left:300px;top:130px;font-size:11px">
      <dt>Mi</dt><span class="sep">:</span><dd>08:00 - 12:00 Uhr</dd>
      <dt>Do</dt><span class="sep">:</span><dd>08:00 - 12:00 Uhr</dd>
      <dt>Fr</dt><span class="sep">:</span><dd>14:00 - 16:00 Uhr</dd>
    </dl>
    <p class="notice notice--plain">
      <span>Wußten Sie schon? Sie können bei uns Termine über</span>
      <span>www.terminofix.de vereinbaren</span>
    </p>
  </section>

</body>
</html>
```